Supplment jar label design (full label)

Hydration (blue) 300g –700ml jar, label size: 10 cm x 27 cm
make label for Kora Vital supps
needs to be full blown label that fits size I noted above
with all claims in attached doc
see attached product info and claims
see QDL & Ember attached as example of similar to what I want
carbon fibre background on label
I have also attached label example this is how i expect to receive designs
where is states SKU on label needs to be in colour above
needs files to able to customise with other SKUs in future
please message me if you have questions
Hydration

```html
<!DOCTYPE html>
<html lang="en">
<head>
<meta charset="utf-8">
<title>Kora Vital Hydration – Full Label</title>
<link href="https://fonts.googleapis.com/css2?family=Anton&family=Montserrat:wght@400;600;700&display=swap" rel="stylesheet">
<style>
  :root {
    --page: #ffffff;
    --carbon-deep: #08090b;
    --carbon-mid: #1a1c20;
    --carbon-light: #2a2d33;
    --ink: #111111;
    --paper: #ffffff;
    --hydration-blue: #1f8fe5;
    --hydration-blue-soft: #7cc6f7;
    --rule: #2f96e6;
  }
  * { box-sizing: border-box; margin: 0; padding: 0; }
  html, body { width: 1200px; height: 1073px; overflow: hidden; background: var(--page); }
  body { font-family: "Montserrat", sans-serif; color: var(--ink); position: relative; }

  .label {
    position: absolute; left: 50px; top: 333px;
    width: 1100px; height: 406px;
    background: var(--paper); overflow: hidden;
  }
  .label-shapes { position: absolute; inset: 0; }

  /* left info column */
  .info-column { position: absolute; left: 30px; top: 18px; width: 240px; font-size: 8.2px; line-height: 1.34; }
  .info-column strong { font-weight: 700; }
  .ingredients { margin-bottom: 9px; }
  .directions {
    background: linear-gradient(135deg, var(--carbon-light), var(--carbon-deep));
    color: var(--paper);
    padding: 5px 10px 5px 8px; border-radius: 0 18px 18px 0; margin-bottom: 13px;
  }
  .section-head { font-weight: 700; font-size: 8.6px; margin-bottom: 8px; }
  .warning { margin-bottom: 10px; }
  .warning mark {
    background: var(--carbon-deep); color: var(--paper); font-weight: 600;
    padding: 0 2px; -webkit-box-decoration-break: clone; box-decoration-break: clone;
  }
  .origin-badge { width: 70px; height: 24px; border: 1px solid var(--ink); border-radius: 2px; display: flex; align-items: center; padding: 0 5px; margin-bottom: 14px; }
  .origin-badge span { display: block; width: 10px; height: 10px; background: var(--hydration-blue); }
  .claims { list-style: none; margin-bottom: 12px; }
  .change-history { font-weight: 700; font-size: 8.2px; margin-bottom: 10px; }
  .barcode-note { font-size: 5.5px; }

  /* brand */
  .brand {
    position: absolute; left: 470px; top: 118px;
    font-family: "Anton", sans-serif; font-size: 80px; line-height: 0.95;
    color: var(--paper); letter-spacing: -1px; text-transform: uppercase; font-weight: 400;
  }

  /* right panels */
  .panel { position: absolute; color: var(--paper); font-size: 7.6px; }
  .panel table { width: 100%; border-collapse: collapse; }
  .product-info { left: 718px; top: 17px; width: 364px; border: 1px solid var(--rule); }
  .product-info h2 { font-size: 12.5px; font-weight: 600; text-align: center; padding: 5px 0 4px; border-bottom: 1px solid var(--rule); }
  .product-info td { border-top: 1px solid var(--rule); padding: 3px 5px; height: 19px; }
  .product-info tr:first-child td { border-top: none; }
  .sku { color: var(--hydration-blue-soft); font-weight: 700; }

  .nutrition { left: 718px; top: 157px; width: 364px; border: 1px solid var(--rule); padding: 4px 5px; }
  .nutrition-head { display: flex; align-items: center; line-height: 1.3; }
  .nutrition-head h3 { font-size: 10px; font-weight: 700; margin-left: 34px; }
  .nutrition th { font-size: 6.2px; font-weight: 700; border: 1px solid var(--rule); padding: 2px; text-align: center; }
  .nutrition th:first-child { border: none; }
  .nutrition td { padding: 0 3px; line-height: 1.22; font-size: 7.6px; }
  .nutrition td:first-child { width: 22%; }

  .history { left: 718px; top: 351px; width: 364px; border: 1px solid var(--rule); }
  .history th, .history td { border: 1px solid var(--rule); padding: 3px 5px; text-align: left; font-weight: 400; height: 19px; }
</style>
</head>
<body>
  <div class="label">
    <svg class="label-shapes" viewBox="0 0 1100 406" width="1100" height="406" role="img" aria-label="Carbon fibre background panel with blue diagonal stripe">
      <defs>
        <linearGradient id="stripe" x1="0" y1="0" x2="0" y2="1">
          <stop offset="0" stop-color="var(--hydration-blue-soft)"/>
          <stop offset="1" stop-color="var(--hydration-blue)"/>
        </linearGradient>
        <linearGradient id="carbon" x1="0" y1="0" x2="1" y2="1">
          <stop offset="0" stop-color="var(--carbon-light)"/>
          <stop offset="0.45" stop-color="var(--carbon-deep)"/>
          <stop offset="0.75" stop-color="var(--carbon-mid)"/>
          <stop offset="1" stop-color="var(--carbon-deep)"/>
        </linearGradient>
      </defs>
      <polygon points="474,0 499,0 338,406 316,406" fill="url(#stripe)"/>
      <polygon points="499,0 1100,0 1100,406 338,406" fill="url(#carbon)"/>
    </svg>

    <section class="info-column">
      <p class="ingredients"><strong>Ingredients:</strong> Electrolyte Minerals (Sodium Chloride, Magnesium Chloride, Potassium Chloride, Calcium Citrate), Acacia Gum, Natural Flavouring, Food Acid (Citric Acid), Sweetener (Thaumatin), Kakadu Fruit Extract.</p>
      <p class="directions"><strong>Directions:</strong> Add 10g (approx. 2 scoops) into 500ml of chilly water depending on your liking, stir or shake to dissolve. Store below 30°C in a cool, dry place.</p>
      <p class="section-head">Recommended Daily Intake: 1 serving.</p>
      <p class="warning">Formulated Supplementary Sports Food.<br>This product is not a sole source of nutrition and should be consumed in conjunction with a nutritious diet and an appropriate physical training or exercise program. Not suitable for children under <mark>15 years of age or pregnant women. Should only be used under medical or dietetic supervision.</mark></p>
      <div class="origin-badge" role="img" aria-label="Country of origin badge"><span></span></div>
      <p class="section-head">Recommended nutritional claims based on FSANZ Schedule 4:</p>
      <ol class="claims">
        <li>1. Gluten Free.</li>
        <li>2. No added artificial flavour, colour &amp; sweetener.</li>
        <li>3. Potassium is necessary for normal water and electrolyte balance.</li>
        <li>4. No Added Sugar</li>
      </ol>
      <p class="change-history">CHANGE HISTORY</p>
      <p class="barcode-note">BAR CODE</p>
    </section>

    <h1 class="brand">Kora<br>Vital</h1>

    <section class="panel product-info">
      <h2>PRODUCT INFORMATION</h2>
      <table>
        <tr><td>Customer: Kora Vital</td></tr>
        <tr><td>Name: <span class="sku">Hydration</span></td></tr>
        <tr><td>Name: <span class="sku">Hydration</span></td></tr>
        <tr><td>Size: 300g</td></tr>
        <tr><td>Date: 20/06/2025</td></tr>
      </table>
    </section>

    <section class="panel nutrition">
      <div class="nutrition-head">
        <p>Servings per package: 30<br>Serving size: 10g</p>
        <h3>NUTRITION INFORMATION</h3>
      </div>
      <table>
        <tr><th></th><th>AVERAGE QUANTITY PER SERVING</th><th>AVERAGE QUANTITY PER 100g</th></tr>
        <tr><td>Energy</td><td>34.6 kJ (8.3 Cal)</td><td>346 kJ (83 Cal)</td></tr>
        <tr><td>Protein</td><td>0.1 g</td><td>1.1 g</td></tr>
        <tr><td>-Gluten</td><td>Nil detected</td><td>Nil detected</td></tr>
        <tr><td>Fat, Total</td><td>0.0 g</td><td>0.0 g</td></tr>
        <tr><td>-Saturated</td><td>0.0 g</td><td>0.0 g</td></tr>
        <tr><td>Carbohydrate</td><td>0.0 g</td><td>0.0 g</td></tr>
        <tr><td>-Sugars</td><td>0.0 g</td><td>0.0 g</td></tr>
        <tr><td>Dietary Fibre</td><td>3.9 g</td><td>39.0 g</td></tr>
        <tr><td>Sodium</td><td>1,200 mg</td><td>12,000 mg</td></tr>
        <tr><td>Potassium</td><td>250 mg</td><td>2,500 mg</td></tr>
        <tr><td>Calcium</td><td>80 mg</td><td>800 mg</td></tr>
        <tr><td>Magnesium</td><td>80 mg</td><td>800 mg</td></tr>
      </table>
    </section>

    <section class="panel history">
      <table>
        <tr><th>Issue Date</th><th>Issue No.</th><th>Issued by</th><th>Position</th><th>Details of Changes</th></tr>
        <tr><td>20/06/2025</td><td>1</td><td>Dana Pirsk</td><td>Innovation Manager</td><td>New Product</td></tr>
      </table>
    </section>
  </div>
</body>
</html>
```